Breezy Puffs Cotton Candy

Looking for a logo design and business cards to help a 13 year old entrepreneur promote her cotton candy business.
Contact Information for Business Card
Name, Phone & Email
Colors
E54698
E96AAD
F1A4CE
F9D9EA
FCEFF6
A7469A
B969AE
D3A5CF
EDDBEB
F8F0F9
6B429C
8869AF
B7A5CE
E3DAEB
F3F0F8
Requirements
Must have
- A fun feel that is appropriate for a teenage girl selling cotton candy

```html
<!DOCTYPE html>
<html lang="en">
<head>
<meta charset="utf-8">
<title>Breezy Puffs Cotton Candy – Business Cards</title>
<link rel="stylesheet" href="https://fonts.googleapis.com/css2?family=Lato:wght@400;700;900&family=Oswald:wght@500&display=swap">
<style>
  :root {
    --backdrop: #262626;
    --card: #111111;
    --pink: #e54698;
    --purple: #6b429c;
    --text-light: #f4f4f4;
    --divider: #8a8a8a;
  }
  * { margin: 0; padding: 0; box-sizing: border-box; }
  html, body {
    width: 1200px; height: 900px; overflow: hidden;
    background: var(--backdrop);
    font-family: "Lato", sans-serif;
  }
  .canvas { position: relative; width: 1200px; height: 900px; }
  .card {
    position: absolute; left: 320px; width: 560px; height: 320px;
    background: var(--card);
    box-shadow: 0 10px 28px rgba(0,0,0,.55);
    overflow: hidden;
  }
  .card--front { top: 100px; }
  .card--back { top: 470px; }
  .card__band {
    position: absolute; left: 0; right: 0; bottom: 0; height: 11px;
    background: var(--pink);
  }
  .brand {
    position: absolute; left: 0; right: 0; top: 62px;
    display: flex; flex-direction: column; align-items: center;
  }
  .brand__dot {
    width: 84px; height: 84px; border-radius: 50%;
    border: 4px solid var(--pink);
    margin-bottom: 14px;
  }
  .brand__name {
    font-weight: 900; color: var(--pink);
    font-size: 34px; line-height: 1.02; text-align: center;
  }
  .person {
    position: absolute; left: 48px; top: 104px; width: 210px; text-align: right;
  }
  .person__name {
    font-family: "Oswald", sans-serif; font-weight: 500;
    color: var(--pink); font-size: 30px; line-height: 1.05;
    text-transform: uppercase; letter-spacing: -0.2px;
  }
  .person__role { color: var(--text-light); font-size: 15px; margin-top: 2px; }
  .divider {
    position: absolute; left: 282px; top: 110px; width: 1px; height: 58px;
    background: var(--divider);
  }
  .contacts {
    position: absolute; left: 306px; top: 114px; list-style: none;
    color: var(--text-light); font-size: 16px;
  }
  .contacts li { display: flex; align-items: center; gap: 9px; height: 26px; }
  .contacts svg { width: 15px; height: 15px; fill: var(--pink); flex: none; }
  .address {
    position: absolute; left: 48px; bottom: 42px;
    color: var(--text-light); font-size: 16px;
  }
</style>
</head>
<body>
<main class="canvas">
  <section class="card card--front" aria-label="Card front">
    <div class="brand">
      <div class="brand__dot"></div>
      <p class="brand__name">Breezy Puffs<br>Cotton Candy</p>
    </div>
    <div class="card__band"></div>
  </section>

  <section class="card card--back" aria-label="Card back">
    <div class="person">
      <h1 class="person__name">Daniel Brooks</h1>
      <p class="person__role">Managing Director</p>
    </div>
    <div class="divider"></div>
    <ul class="contacts">
      <li>
        <svg viewBox="0 0 24 24" aria-hidden="true"><path d="M6.6 10.8a15.1 15.1 0 0 0 6.6 6.6l2.2-2.2a1 1 0 0 1 1-.25 11.4 11.4 0 0 0 3.6.57 1 1 0 0 1 1 1V20a1 1 0 0 1-1 1A17 17 0 0 1 3 4a1 1 0 0 1 1-1h3.5a1 1 0 0 1 1 1c0 1.25.2 2.45.57 3.57a1 1 0 0 1-.25 1z"/></svg>
        044-987 654 321
      </li>
      <li>
        <svg viewBox="0 0 24 24" aria-hidden="true"><path d="M2 5h20v14H2z M3.5 6.5 12 13l8.5-6.5" fill="none" stroke="#e54698" stroke-width="2"/><path d="M2 5h20v2l-10 7L2 7z"/></svg>
        hello@breezypuffs.com
      </li>
    </ul>
    <p class="address">87, Maple Lane, Sample Town, 30218</p>
    <div class="card__band"></div>
  </section>
</main>
</body>
</html>
```